Vellora Labs - Mushroom Supplement Packaging

Our brand is called Vellora Labs. I've added a couple different logos that you can use. We are creating a line up of Mushroom Supplement products. I will add the entire line-up of products here. I've added examples of other products and packaging shape types I can purchase. Give me different options for packaging that is minimalist and clean for this brand that makes it look really well made and clean and make people want to buy.

Product 1 Lions Mane 1g
Product 2 Cordyceps 1g
Product 3 Chaga 1g
Product 4 Turkey Tail 1g
Product 5 Reishi 1g
Product 6 Maitake 1g
Product 7 Shiitake 1g

Product 8 (Mix) Lions Mane 143mg
Cordyceps 143mg
Chaga 143mg
Turkey Tail 143mg
Reishi 143mg
Maitake 143mg
Shiitake 143mg

```html
<!DOCTYPE html>
<html lang="en">
<head>
<meta charset="UTF-8">
<title>Vellora Labs – Lions Mane Label</title>
<link rel="stylesheet" href="https://fonts.googleapis.com/css2?family=Cinzel:wght@600&family=Oswald:wght@500&family=Outfit:wght@400;600&display=swap">
<style>
  :root {
    --backdrop: #5c5c5c;
    --label-white: #f1f1f2;
    --band-green: #93c6a2;
    --band-green-light: #a9d4b5;
    --ink: #232323;
    --ink-green: #3a5a42;
    --ink-soft: #3c3c3c;
    --rule: #5e7f66;
    --badge: #1f1f1f;
    --badge-text: #ffffff;
  }
  * { margin: 0; padding: 0; box-sizing: border-box; }
  html, body {
    width: 1200px; height: 1200px; overflow: hidden;
    background: var(--backdrop);
  }
  .label {
    position: absolute; left: 150px; top: 80px;
    width: 900px; height: 1040px;
    background: var(--label-white);
    overflow: hidden;
  }
  .label__band {
    position: absolute; left: 0; right: 0; top: 564px; bottom: 0;
    background: linear-gradient(100deg, var(--band-green) 0%, var(--band-green-light) 55%, var(--band-green) 100%);
  }
  .count-badge {
    position: absolute; left: 746px; top: 0;
    width: 66px; height: 127px;
    background: var(--badge);
    border-radius: 0 0 33px 33px;
    color: var(--badge-text);
    font-family: 'Outfit', sans-serif;
    text-align: center;
    padding-top: 38px;
  }
  .count-badge__number { display: block; font-size: 25px; font-weight: 600; line-height: 1; }
  .count-badge__unit { display: block; font-size: 12px; font-weight: 400; margin-top: 4px; }
  .brand-name {
    position: absolute; left: 220px; top: 118px; width: 400px;
    text-align: center;
    font-family: 'Oswald', sans-serif; font-weight: 500;
    font-size: 64px; line-height: 1;
    color: var(--ink);
    text-transform: uppercase;
  }
  .hero-art {
    position: absolute; left: 254px; top: 326px;
    width: 332px; height: 348px;
    border-radius: 46% 46% 30% 30%;
    background: radial-gradient(ellipse at 50% 45%, #e6e6e6 0%, #cfcfcf 60%, rgba(200,200,200,0.6) 100%);
  }
  .product-name {
    position: absolute; left: 0; width: 840px; top: 742px;
    text-align: center;
    font-family: 'Cinzel', serif; font-weight: 600;
    font-size: 92px; line-height: 1;
    color: var(--ink);
  }
  .benefits {
    position: absolute; left: 0; width: 840px; top: 862px;
    text-align: center;
    font-family: 'Outfit', sans-serif; font-weight: 600;
    font-size: 36px; color: var(--ink-green);
  }
  .divider {
    position: absolute; left: 199px; top: 928px;
    width: 442px; height: 1.5px; background: var(--rule);
  }
  .category {
    position: absolute; left: 0; width: 840px; top: 952px;
    text-align: center;
    font-family: 'Outfit', sans-serif; font-weight: 400;
    font-size: 30px; color: var(--ink-soft);
  }
  .net-weight {
    position: absolute; right: 50px; top: 952px;
    font-family: 'Outfit', sans-serif; font-weight: 400;
    font-size: 28px; color: var(--ink);
  }
</style>
</head>
<body>
  <main class="label">
    <div class="label__band"></div>

    <div class="count-badge">
      <span class="count-badge__number">60</span>
      <span class="count-badge__unit">Capsules</span>
    </div>

    <div class="brand-name">Vellora Labs</div>

    <div class="hero-art" role="img" aria-label="Line illustration of a cluster of mushrooms surrounded by leaves and small flowers"></div>

    <h1 class="product-name">LIONS MANE</h1>
    <p class="benefits">Focus, Clarity &amp; Mood</p>
    <div class="divider"></div>
    <p class="category">Dietary Supplement</p>
    <p class="net-weight">60g</p>
  </main>
</body>
</html>
```